Quote Cards for Social Media RV

I would like to put these quotes over one of the pictures attached; One Quote per picture, and I want the quote to be bold or easy to read as well. I provided a few reference graphics that I really like as examples below. In very small letters at the bottom add @RVCarloweDaily

All of the pictures are attached; you can pick any photo and add one quote to it; but no stock photography

Target Market(s)

women trying to lose weight

Requirements
Must have
• quotes and pictures attached
Should not have
• no stock photography

```html
<!DOCTYPE html>
<html lang="en">
<head>
<meta charset="UTF-8">
<title>Quote Card – Wake Up</title>
<link rel="stylesheet" href="https://fonts.googleapis.com/css2?family=Playfair+Display:ital,wght@1,700;1,900&family=Source+Serif+4:wght@400&display=swap">
<style>
  :root {
    --frame: #000000;
    --bg-light: #f4f4f4;
    --bg-mid: #d6d6d6;
    --bg-dark: #a9a9a9;
    --pink: #ff3aa6;
    --pink-light: #ff8fd0;
    --pink-pale: #ffd3ec;
    --ink: #1c1c1c;
    --photo-top: #b8b8b8;
    --photo-bottom: #5e5e5e;
    --bottle-top: #ffffff;
    --bottle-bottom: #e7d6e2;
  }
  html, body {
    margin: 0;
    padding: 0;
    width: 1200px;
    height: 1200px;
    overflow: hidden;
    background: var(--frame);
  }
  .card {
    position: relative;
    width: 1200px;
    height: 1200px;
    background: var(--frame);
    overflow: hidden;
  }
  .card-art,
  .handle-tab {
    position: absolute;
    inset: 0;
  }
  .model-photo {
    position: absolute;
    left: 650px;
    top: 20px;
    width: 530px;
    height: 990px;
    border-radius: 240px 240px 40px 40px;
    background: linear-gradient(180deg, var(--photo-top), var(--photo-bottom));
  }
  .product-photo {
    position: absolute;
    left: 92px;
    top: 665px;
    width: 478px;
    height: 325px;
    border-radius: 24px;
    background: linear-gradient(180deg, var(--bottle-top), var(--bottle-bottom));
  }
  .headline {
    position: absolute;
    left: 100px;
    top: 262px;
    margin: 0;
    font-family: "Playfair Display", Georgia, serif;
    font-style: italic;
    font-weight: 900;
    font-size: 122px;
    line-height: 1;
    color: var(--pink);
  }
  .headline-rule {
    position: absolute;
    left: 108px;
    top: 403px;
    width: 400px;
    height: 5px;
    background: var(--pink);
  }
  .quote {
    position: absolute;
    left: 94px;
    top: 425px;
    margin: 0;
    font-family: "Source Serif 4", Georgia, serif;
    font-weight: 400;
    font-size: 46px;
    line-height: 66px;
    color: var(--ink);
  }
  .handle {
    position: absolute;
    left: 90px;
    top: 1082px;
    margin: 0;
    font-family: "Playfair Display", Georgia, serif;
    font-style: italic;
    font-weight: 700;
    font-size: 28px;
    line-height: 36px;
    letter-spacing: 0.5px;
    color: var(--pink);
  }
</style>
</head>
<body>
<main class="card">
  <svg class="card-art" width="1200" height="1200" viewBox="0 0 1200 1200" aria-hidden="true">
    <defs>
      <radialGradient id="backdrop" cx="0.35" cy="0.35" r="0.8">
        <stop offset="0" stop-color="#f4f4f4"/>
        <stop offset="0.6" stop-color="#d6d6d6"/>
        <stop offset="1" stop-color="#a9a9a9"/>
      </radialGradient>
      <linearGradient id="band" x1="0" y1="0" x2="1" y2="0">
        <stop offset="0" stop-color="#ff8fd0"/>
        <stop offset="1" stop-color="#ff3aa6"/>
      </linearGradient>
    </defs>
    <rect class="backdrop" x="20" y="20" width="1160" height="1160" fill="url(#backdrop)"/>
    <path class="wave-pale" d="M20 870 C320 830 640 1000 1180 800 L1180 1180 L20 1180 Z" fill="#ffd3ec"/>
    <path class="wave-band" d="M20 895 C330 860 650 1030 1180 830 L1180 1180 L20 1180 Z" fill="url(#band)"/>
    <path class="wave-line" d="M20 925 C360 900 700 1060 1180 900" fill="none" stroke="#ffffff" stroke-opacity="0.6" stroke-width="4"/>
  </svg>

  <div class="model-photo" role="img" aria-label="Smiling woman in a grey turtleneck and high-waisted black trousers, hand on hip"></div>

  <h1 class="headline">Wake up</h1>
  <div class="headline-rule"></div>
  <p class="quote">tomorrow with a flatter<br>belly- yes, this overnight<br>remedy works like magic!</p>

  <div class="product-photo" role="img" aria-label="Three white supplement bottles with pink labels"></div>

  <svg class="handle-tab" width="1200" height="1200" viewBox="0 0 1200 1200" aria-hidden="true">
    <path d="M0 1000 L530 1000 Q590 1000 590 1060 L590 1200 L0 1200 Z" fill="#000000"/>
    <rect x="0" y="1180" width="1200" height="20" fill="#000000"/>
    <rect x="1180" y="0" width="20" height="1200" fill="#000000"/>
  </svg>

  <p class="handle">@RVCarloweDaily</p>
</main>
</body>
</html>
```